Design an Eye-Catching Banner Ad

Morvanta Security provides network security for small and medium businesses. We sell through the IT channel -- which means our product is sold and serviced by IT service companies across the US. We consider these companies our "partners" or "reseller partners." They buy our product and service, then deliver it to their clients. Our one and only product is the TrellisCore UTM firewall.

As part of the latest release of TrellisCore, we’ve introduced the Bluefinch feature. We want to raise awareness of Bluefinch online on partner sites.

The landing page at www.morvanta-demo.com/bluefinch will give you more information about the feature.

Target Market(s)

IT security motivated prospects who will see the value of the Bluefinch product.

Requirements
Must have
• Morvanta logo
Bluefinch logo

This ad will be posted on HTTPS://quillorbit-demo.tech is the site

Need two graphics One is 728x90, and the other is 160x600

```html
<!DOCTYPE html>
<html lang="en">
<head>
<meta charset="utf-8">
<title>Quillorbit – News and Insights for Technology Services Providers</title>
<link rel="stylesheet" href="https://fonts.googleapis.com/css2?family=PT+Serif:ital,wght@0,400;0,700;1,400;1,700&family=Source+Sans+Pro:wght@400;600;700&family=Lato:wght@400;700;900&display=swap">
<style>
:root{
  --ink:#111111;
  --text:#2a2a2a;
  --muted:#6b6b6b;
  --rule:#dddddd;
  --paper:#ffffff;
  --ad-navy:#2b2a44;
  --ad-navy-deep:#1f1e33;
  --ad-red:#d3343f;
  --ad-white:#ffffff;
  --brand-red:#d3202e;
  --brand-blue:#1f3f8f;
}
*{box-sizing:border-box;margin:0;padding:0}
html,body{width:1200px;height:967px;overflow:hidden;background:var(--paper)}
body{position:relative;font-family:"PT Serif",Georgia,serif;color:var(--text)}
a{color:inherit;text-decoration:none}

.top-nav{position:absolute;left:33px;top:25px;display:flex;gap:12px;font-family:"Source Sans Pro",Arial,sans-serif;font-size:11px;letter-spacing:.6px;text-transform:uppercase;color:var(--ink)}
.top-nav .search{font-weight:700;display:flex;align-items:center;gap:5px;margin-right:7px}
.top-nav .current{text-decoration:underline}

.social{position:absolute;left:1050px;top:23px;display:flex;gap:8px}
.social span{width:24px;height:24px;border:2px solid var(--ink);border-radius:5px;display:block}
.social span::after{content:"";display:block;width:10px;height:10px;margin:5px;background:var(--ink);border-radius:50%}

.masthead{position:absolute;left:0;width:1276px;top:56px;text-align:center}
.brand{display:inline-flex;align-items:center;gap:8px;font-family:"PT Serif",Georgia,serif;font-weight:700;font-size:26px;line-height:40px;color:var(--brand-blue);letter-spacing:1px}
.brand .mark{width:22px;height:22px;background:var(--brand-red);border-radius:50%}
.tagline{margin-top:12px;font-style:italic;font-size:11.5px;color:var(--ink)}
.dateline{position:absolute;left:33px;top:127px;font-family:"Source Sans Pro",Arial,sans-serif;font-weight:600;font-size:11px;color:var(--ink)}
.masthead-rule{position:absolute;left:33px;top:149px;width:1167px;height:2px;background:var(--ink)}

.section-nav{position:absolute;left:290px;top:166px;display:flex;gap:23px;font-family:"Source Sans Pro",Arial,sans-serif;font-size:15px;color:var(--ink)}
.header-shade{position:absolute;left:0;top:197px;width:1200px;height:2px;background:linear-gradient(#e8e8e8,transparent)}

.col-left{position:absolute;left:36px;top:196px;width:266px;height:771px;overflow:hidden}
.col-left .inner{margin-top:-6px}
.side-post{margin-bottom:24px}
.side-post h3{font-weight:700;font-style:italic;font-size:20px;line-height:24px;color:var(--ink)}
.byline{font-family:"PT Serif",Georgia,serif;font-size:12px;color:var(--muted);text-transform:uppercase;letter-spacing:.1px}
.side-post .byline{margin-top:6px}
.side-post p{margin-top:9px;font-size:15px;line-height:24px;color:var(--ink)}
.comments{margin-top:4px;font-style:italic;font-size:11.5px;color:var(--ink);display:flex;align-items:center;gap:5px}

.col-divider{position:absolute;top:199px;width:1px;height:768px;background:var(--rule)}

.col-main{position:absolute;left:353px;top:204px;width:569px}
.col-main .top-rule{height:1px;background:var(--rule)}
.leaderboard{margin:14px 0 0 6px;width:558px;height:74px}
.post{border-top:1px solid var(--rule);padding:20px 0 18px}
.posts{margin-top:49px}
.post h2{font-weight:400;font-size:28px;line-height:38px;color:var(--ink)}
.post p{margin-top:12px;font-size:15px;line-height:24px;color:var(--ink)}

.col-right{position:absolute;left:976px;top:222px;width:224px}
.col-right label{display:block;font-size:15px;color:var(--ink)}
.email-field{margin-top:3px;height:36px;border:1px solid var(--rule);border-right:none;padding:0 12px;font-family:"Source Sans Pro",Arial,sans-serif;font-size:13px;color:#666;display:flex;align-items:center}
.digest-btn{margin-top:24px;width:155px;height:37px;background:var(--ink);color:var(--ad-white);font-family:"Source Sans Pro",Arial,sans-serif;font-weight:700;font-size:13px;display:flex;align-items:center;justify-content:center}
.skyscraper{position:absolute;left:1026px;top:356px;width:174px;height:611px}

.ad{background:radial-gradient(ellipse at 85% 95%,#5a3046 0%,var(--ad-navy) 45%,var(--ad-navy-deep) 100%);color:var(--ad-white);font-family:"Lato",Arial,sans-serif;position:relative;overflow:hidden}
.ad .helmet{background:linear-gradient(160deg,#e0444d,#9c1f2a);border-radius:45% 45% 30% 30%}
.ad .product{font-weight:400;color:var(--ad-white)}
.ad .headline{font-weight:900;color:var(--ad-white)}
.ad .vendor{font-weight:400;color:var(--ad-white);white-space:nowrap}

.leaderboard .helmet{position:absolute;left:74px;top:4px;width:36px;height:62px}
.leaderboard .product{position:absolute;left:123px;top:44px;font-size:14px}
.leaderboard .headline{position:absolute;left:226px;top:25px;font-size:17px;line-height:19px}
.leaderboard .vendor{position:absolute;right:14px;top:10px;font-size:11px}
.leaderboard .swirl{position:absolute;right:0;bottom:0;width:170px;height:74px;background:linear-gradient(135deg,transparent 40%,rgba(211,52,63,.35) 70%,transparent 100%)}

.skyscraper .helmet{position:absolute;left:28px;top:84px;width:104px;height:150px}
.skyscraper .product{position:absolute;left:0;width:160px;text-align:center;top:235px;font-size:14px}
.skyscraper .headline{position:absolute;left:0;width:160px;text-align:center;top:280px;font-size:24px;line-height:29px}
.skyscraper .swirl{position:absolute;left:0;bottom:0;width:174px;height:190px;background:linear-gradient(160deg,transparent 20%,rgba(211,52,63,.35) 60%,transparent 95%)}
.skyscraper .vendor{position:absolute;left:0;width:160px;text-align:center;top:578px;font-size:11px}
</style>
</head>
<body>

<nav class="top-nav">
  <a class="search" href="#"><svg width="11" height="11" viewBox="0 0 11 11"><circle cx="4.5" cy="4.5" r="3.5" fill="none" stroke="#111" stroke-width="1.8"/><line x1="7" y1="7" x2="10.3" y2="10.3" stroke="#111" stroke-width="1.8"/></svg>Search</a>
  <a class="current" href="#">Home</a>
  <a href="#">About</a>
  <a href="#">Contact</a>
  <a href="#">Advertise</a>
</nav>

<div class="social" aria-label="Social links"><span></span><span></span><span></span><span></span><span></span></div>

<header class="masthead">
  <div class="brand"><span class="mark"></span>QUILLORBIT</div>
  <div class="tagline">News and Insights for Technology Services Providers</div>
</header>
<div class="dateline">November 13, 2020</div>
<div class="masthead-rule"></div>

<nav class="section-nav">
  <a href="#">Business Strategy</a>
  <a href="#">Diversity</a>
  <a href="#">Regulation</a>
  <a href="#">Security</a>
  <a href="#">Blocking &amp; Tackling</a>
  <a href="#">Editorial</a>
  <a href="#">Podcast</a>
</nav>
<div class="header-shade"></div>

<aside class="col-left">
  <div class="inner">
    <article class="side-post">
      <h3>Halcyon Soft &amp; Orbisearch's Play: Solution Provider Insights on the new platforms</h3>
      <div class="byline">By Reed Halvorsen</div>
      <p>I was asked by a Backerly about my thinking on Orbisearch's recent re-branding of O Suite to "Orbisearch Workspace". The Backerly was…</p>
      <div class="comments"><svg width="11" height="10" viewBox="0 0 11 10"><path d="M5.5 1C2.8 1 1 2.6 1 4.4c0 1 .5 1.8 1.4 2.4L2 9l2.4-1.5c.4.1.7.1 1.1.1 2.7 0 4.5-1.6 4.5-3.2S8.2 1 5.5 1z" fill="none" stroke="#111"/></svg>Leave a Comment</div>
    </article>
    <article class="side-post">
      <h3>What a K Shaped Recovery Means for Tech Services Companies</h3>
      <div class="byline">By Reed Halvorsen</div>
      <p>Let’s talk about the recovery. Here’s the question I was asked. “What does a K shaped recovery looks like? Our industry, and a few others,…</p>
      <div class="comments"><svg width="11" height="10" viewBox="0 0 11 10"><path d="M5.5 1C2.8 1 1 2.6 1 4.4c0 1 .5 1.8 1.4 2.4L2 9l2.4-1.5c.4.1.7.1 1.1.1 2.7 0 4.5-1.6 4.5-3.2S8.2 1 5.5 1z" fill="none" stroke="#111"/></svg>Leave a Comment</div>
    </article>
    <article class="side-post">
      <h3>Don’t Start an MSP</h3>
      <div class="byline">By Reed Halvorsen</div>
      <p>This came from a discussion with a consulting organization about "advice for immature MSPs". And I just could not resist. When all the messaging is…</p>
      <div class="comments"><svg width="11" height="10" viewBox="0 0 11 10"><path d="M5.5 1C2.8 1 1 2.6 1 4.4c0 1 .5 1.8 1.4 2.4L2 9l2.4-1.5c.4.1.7.1 1.1.1 2.7 0 4.5-1.6 4.5-3.2S8.2 1 5.5 1z" fill="none" stroke="#111"/></svg>Leave a Comment</div>
    </article>
    <article class="side-post">
      <h3>Channel is an overloaded term</h3>
    </article>
  </div>
</aside>

<div class="col-divider" style="left:318px"></div>
<div class="col-divider" style="left:957px"></div>

<main class="col-main">
  <div class="top-rule"></div>
  <div class="ad leaderboard">
    <div class="helmet" role="img" aria-label="Red Bluefinch helmet illustration"></div>
    <div class="product">Bluefinch™</div>
    <div class="headline">The Small Business Solution<br>to Secure Remote Access</div>
    <div class="swirl" role="img" aria-label="Red flowing line pattern"></div>
    <div class="vendor">Morvanta Security</div>
  </div>

  <div class="posts">
    <article class="post">
      <h2>Vantor is going virtual for 2021</h2>
      <div class="byline">By Reed Halvorsen on November 12, 2020</div>
      <p>The Organizers of the Vantor Conference given up on a physical event next year, reversing the decision to push the conference until the spring.&nbsp; Quoting…</p>
    </article>
    <article class="post">
      <h2>How bad is the cybersecurity job market?</h2>
      <div class="byline">By Reed Halvorsen on November 12, 2020</div>
      <p>New data from SkillMapper focuses on the supply and demand in the cybersecurity job market.&nbsp;&nbsp;&nbsp; The bad news – the talent shortage is nearing a…</p>
    </article>
    <article class="post">
      <h2>Corvane says up when data says down</h2>
      <div class="byline">By Reed Halvorsen on November 11, 2020</div>
      <p>Longtime listeners know I love a good analyst report, and Corvane recently presented at a channel forum and, as might be expected, touted the channel’s…</p>
    </article>
    <article class="post">
      <h2>TechNorth: How to build a SMB Cloud Strategy</h2>
      <div class="byline">By Reed Halvorsen on November 11, 2020</div>
      <p>TechNorth has released new insights into the development of an SMB Cloud</p>
    </article>
  </div>
</main>

<aside class="col-right">
  <label>Email address:</label>
  <div class="email-field">Your email address</div>
  <div class="digest-btn">Get the Daily Digest</div>
</aside>

<div class="ad skyscraper">
  <div class="helmet" role="img" aria-label="Red Bluefinch helmet illustration"></div>
  <div class="product">Bluefinch™</div>
  <div class="headline">The Small<br>Business<br>Solution<br>to Secure<br>Remote<br>Access</div>
  <div class="swirl" role="img" aria-label="Red flowing line pattern"></div>
  <div class="vendor">Morvanta Security</div>
</div>

</body>
</html>
```